Tavor Management - Managing Urban Projects for the City of Modiin

Tavor Management needs a website that projects its professionalism and innovation to the residents of the city of Modiin. The design needs include: 1) a homepage design, 2) ~12 customized icons used on the homepage, 3) a layered image (city landscape with company logo on it) used as a fullwidth background image on the homepage. The client wants a site that is pleasant on the eye and easy to navigate. The client wants the site to project the organization as being professional and innovative.

Target Market(s)

adult residents of the city of modiin, israel

Industry/Entity Type

management of urban projects

Number of Pages Required

1 page

Font styles to use
Sans Serif

Requirements
Must have
• psd of design and psd of main fullwidth background image on the homepage
Nice to have
• icons for navigation bar and homepage teasers
Should not have
• colors should match the logo attached, font should be modern

```html
<!DOCTYPE html>
<html lang="he" dir="rtl">
<head>
<meta charset="utf-8">
<title>מנהלת תבור</title>
<link href="https://fonts.googleapis.com/css2?family=Heebo:wght@300;400;500;700;800&display=swap" rel="stylesheet">
<style>
:root{
  --green:#3ea843;
  --green-dark:#2b8a33;
  --green-light:#5cc65a;
  --side-top:#3da142;
  --side-bottom:#5fc85c;
  --dark:#353535;
  --text:#333;
  --muted:#666;
  --footer:#e7e7e7;
  --white:#fff;
}
*{box-sizing:border-box;margin:0;padding:0}
html,body{width:1200px;height:2633px;overflow:hidden}
body{position:relative;font-family:'Heebo',sans-serif;color:var(--text);background:var(--white)}

/* sidebar */
.sidebar{position:absolute;right:0;top:0;width:116px;height:2633px;background:linear-gradient(180deg,var(--side-top),var(--side-bottom) 40%,var(--side-bottom));z-index:5}
.nav-item{height:75px;border-bottom:1px solid rgba(255,255,255,.25);display:flex;flex-direction:column;align-items:center;justify-content:center;color:#fff;font-size:14px;font-weight:500;text-align:center;line-height:1.05}
.nav-item svg{width:24px;height:24px;margin-bottom:5px;fill:none;stroke:#fff;stroke-width:1.6}
.nav-item.tall{height:88px}

/* hero */
.hero{position:absolute;left:0;top:0;width:1085px;height:745px;background:linear-gradient(180deg,#8fb2d2 0%,#c3d3df 30%,#9b9a86 45%,#6f7563 60%,#4f6a3a 80%,#3f5a2d 100%)}
.hero-notch{position:absolute;left:512px;top:715px;width:86px;height:40px;background:#fff;border-radius:43px 43px 0 0}
.mouse{position:absolute;left:548px;top:725px;width:12px;height:20px;border:1.5px solid #555;border-radius:6px}
.brand{position:absolute;left:392px;top:208px;width:320px;text-align:center;color:var(--green);font-weight:800;font-size:34px;line-height:1.1}
.brand-sub{position:absolute;left:392px;top:246px;width:320px;text-align:center;color:#555;font-size:11px;letter-spacing:3px}
.teaser{position:absolute;top:372px;width:188px;height:168px;background:rgba(30,30,30,.78);border:1.5px solid var(--green);border-radius:6px;color:#fff;text-align:center;font-size:19px;line-height:1.25;padding-top:28px}
.teaser svg{width:54px;height:52px;display:block;margin:0 auto 8px}
.teaser .bar{width:30px;height:3px;background:var(--green-light);margin:10px auto 0}

/* about */
.about-frame-a{position:absolute;left:81px;top:826px;width:133px;height:122px;background:var(--green)}
.about-frame-b{position:absolute;left:81px;top:1070px;width:110px;height:122px;background:var(--green)}
.about-photo{position:absolute;left:92px;top:837px;width:441px;height:343px;border-radius:45px 0 0 0;background:linear-gradient(180deg,#b9cde0 0%,#cfd9df 18%,#9aa08c 30%,#7d9a5b 50%,#5f8a3c 75%,#b8b8b0 92%,#888 100%)}
.eyebrow{color:var(--green);font-size:15px}
.h2{font-size:31px;font-weight:500;color:#2b2b2b;line-height:1.1}
.about-text{position:absolute;left:585px;top:855px;width:440px}
.about-text .rule{width:58px;height:2px;background:var(--green);margin:10px 0 22px auto}
.about-text p{font-size:13px;line-height:1.45;color:#444;margin-bottom:14px}
.btn-green{display:inline-block;background:linear-gradient(90deg,var(--green-dark),var(--green-light));color:#fff;border-radius:20px;font-size:18px;text-align:center}

/* projects */
.projects-band{position:absolute;left:0;top:1263px;width:1085px;height:323px;background:var(--dark)}
.projects-head{position:absolute;left:0;top:1310px;width:1085px;text-align:center;color:#fff}
.projects-head .rule{width:64px;height:2px;background:var(--green);margin:14px auto 0}
.card-photo{position:absolute;top:1424px;width:293px;height:190px}
.card-box{position:absolute;top:1585px;width:253px;height:122px;background:#fff;border:1px solid #ccc;text-align:center;padding-top:24px}
.card-box h3{font-size:19px;font-weight:400;color:#333}
.card-box p{font-size:8px;color:#777;margin:4px 0 10px}
.card-box .btn-green{width:104px;height:26px;font-size:14px;line-height:26px}
.card-box.active{background:linear-gradient(180deg,#3da844,#2f8f34);border-color:transparent;color:#fff}
.card-box.active h3,.card-box.active p{color:#fff}
.card-box.active .btn-green{background:none;border:1px solid #fff}

/* contact */
.footer-bg{position:absolute;left:0;top:2160px;width:1085px;height:473px;background:var(--footer)}
.contact{position:absolute;left:88px;top:1795px;width:914px;height:500px;border-radius:6px;background:linear-gradient(180deg,#3fa64a 0%,#38a03f 65%,#2f8e38 100%);color:#fff;text-align:center}
.contact .eyebrow{color:#fff;padding-top:53px}
.contact .h2{color:#fff}
.contact .rule{width:58px;height:2px;background:#fff;margin:2px auto 0}
.contact .lead{font-size:13px;margin-top:16px}
.field{position:absolute;background:#fff;border:1px solid #ddd;color:#555;font-size:14px;text-align:right;padding:14px 18px 0 0;display:flex;gap:6px}
.field svg{width:14px;height:14px;fill:none;stroke:#999;stroke-width:1.6;margin-top:2px}
.send{position:absolute;left:374px;top:393px;width:153px;height:40px;background:#111;border-radius:20px;font-size:18px;line-height:40px}

/* footer */
.fcol{position:absolute;top:2345px;border-right:2px solid var(--green);padding-right:14px}
.fcol h4{font-size:22px;font-weight:500;color:#333;line-height:1;margin-bottom:20px}
.fcol p,.fcol li{font-size:12.5px;color:#333;line-height:1.75;list-style:none}
.divider{position:absolute;top:2295px;width:1px;height:295px;background:#ccc}
.ico-circle{display:inline-flex;width:30px;height:30px;border-radius:50%;background:var(--green);align-items:center;justify-content:center;vertical-align:middle;margin-left:8px}
.ico-circle svg{width:15px;height:15px;fill:#fff}
.copy{position:absolute;left:0;top:2590px;width:1085px;border-top:1px solid #ccc;text-align:center;font-size:12px;color:#555;padding-top:14px}
.to-top{position:absolute;left:1009px;top:2559px;width:32px;height:32px;border-radius:50%;background:var(--green)}
</style>
</head>
<body>

<section class="hero" role="img" aria-label="צילום אווירי של העיר עם פארק ואגם">
  <div class="brand">מנהלת תבור</div>
  <div class="brand-sub">נווה תבור | גבעת הדר | רמת אלון</div>

  <div class="teaser" style="left:167px">
    <svg viewBox="0 0 54 52"><rect x="20" y="6" width="18" height="40" fill="#fff"/><g fill="#3ea843"><rect x="24" y="12" width="10" height="2"/><rect x="24" y="18" width="10" height="2"/><rect x="24" y="24" width="10" height="2"/><rect x="24" y="30" width="10" height="2"/><circle cx="12" cy="30" r="5"/><rect x="11" y="33" width="2" height="13"/></g><rect x="6" y="45" width="42" height="2" fill="#3ea843"/></svg>
    פארק טכנולוגי<div class="bar"></div>
  </div>
  <div class="teaser" style="left:369px">
    <svg viewBox="0 0 54 52"><circle cx="27" cy="8" r="5" fill="#fff"/><path d="M22 16h10l3 16h-4l-2 16h-3l-1-14-1 14h-3l-2-16h-4z" fill="#fff"/><rect x="34" y="24" width="12" height="16" fill="#3ea843"/><rect x="8" y="26" width="10" height="13" fill="#3ea843"/></svg>
    מרכז מסחרי<div class="bar"></div>
  </div>
  <div class="teaser" style="left:573px">
    <svg viewBox="0 0 54 52"><rect x="12" y="4" width="30" height="38" rx="7" fill="#fff"/><rect x="16" y="10" width="22" height="14" rx="2" fill="#3ea843"/><circle cx="19" cy="34" r="3" fill="#3ea843"/><circle cx="35" cy="34" r="3" fill="#3ea843"/><rect x="15" y="42" width="5" height="6" fill="#fff"/><rect x="34" y="42" width="5" height="6" fill="#fff"/></svg>
    מרכז התחבורה<div class="bar"></div>
  </div>
  <div class="teaser" style="left:776px">
    <svg viewBox="0 0 54 52"><rect x="4" y="20" width="6" height="12" rx="2" fill="#3ea843"/><rect x="10" y="16" width="7" height="20" rx="2" fill="#3ea843"/><rect x="17" y="24" width="20" height="4" fill="#fff"/><rect x="37" y="16" width="7" height="20" rx="2" fill="#3ea843"/><rect x="44" y="20" width="6" height="12" rx="2" fill="#3ea843"/></svg>
    מרכז ספורט<br>ונופש<div class="bar"></div>
  </div>
</section>
<div class="hero-notch"></div>
<div class="mouse"></div>

<nav class="sidebar">
  <div class="nav-item"><svg viewBox="0 0 24 24"><path d="M3 11l9-8 9 8M6 9v11h12V9"/></svg>בית</div>
  <div class="nav-item"><svg viewBox="0 0 24 24"><circle cx="12" cy="12" r="9"/><path d="M12 11v6M12 7v1"/></svg>אודות</div>
  <div class="nav-item"><svg viewBox="0 0 24 24"><path d="M4 10h4l9-5v14l-9-5H4zM8 14l2 6"/></svg>מידע לעסקים</div>
  <div class="nav-item"><svg viewBox="0 0 24 24"><circle cx="12" cy="12" r="4"/><circle cx="12" cy="12" r="8" stroke-dasharray="3 2"/></svg>ניהול פרויקטים</div>
  <div class="nav-item tall"><svg viewBox="0 0 24 24"><rect x="4" y="6" width="7" height="15"/><rect x="13" y="3" width="7" height="18"/></svg>הנדסה<br>ותכנון</div>
  <div class="nav-item"><svg viewBox="0 0 24 24"><circle cx="12" cy="7" r="3"/><circle cx="7" cy="16" r="3"/><circle cx="17" cy="16" r="3"/></svg>מכרזים</div>
  <div class="nav-item"><svg viewBox="0 0 24 24"><rect x="4" y="4" width="16" height="16"/><path d="M7 8h10M7 12h10M7 16h6"/></svg>שילוט ופרסום</div>
  <div class="nav-item"><svg viewBox="0 0 24 24"><rect x="4" y="4" width="16" height="17"/><path d="M7 16l4-4 3 3 4-5"/></svg>פרויקטים</div>
  <div class="nav-item"><svg viewBox="0 0 24 24"><path d="M5 4l4 1 1 4-2 2a12 12 0 0 0 5 5l2-2 4 1 1 4-3 1C10 20 4 14 4 7z"/></svg>צור קשר</div>
</nav>

<div class="about-frame-a"></div>
<div class="about-frame-b"></div>
<div class="about-photo" role="img" aria-label="צילום אווירי של אזור התעשייה והפארק"></div>
<div class="about-text">
  <div class="eyebrow">אודות</div>
  <div class="h2">אודות מנהלת תבור</div>
  <div class="rule"></div>
  <p>מנהלת תבור אחראית על ניהול פארק הטכנולוגיה (אלונים), מרכז בניין (הגפן), מרכז הבנייה, מרכז התחבורה, הכיכרות לכל אורכן ושלושת מרכזי הספורט והנופש.</p>
  <p>מטרת המנהלת היא לקדם את פארק הטכנולוגיה ואת המרכזים העירוניים ולהוביל אותם לרמה הגבוהה ביותר, תוך ליווי עסקים ותושבים לאורך כל הדרך – שירות מקצועי, זמין וידידותי.</p>
  <p>בנוסף, המנהלת מלווה את כלל היזמים והעסקים במתחמים השונים ומספקת שירותי תחזוקה, ניקיון, שילוט, ביטחון ושירותי מידע שוטפים.</p>
  <span class="btn-green" style="width:144px;height:38px;line-height:38px;margin-top:16px">קרא עוד</span>
</div>

<div class="projects-band"></div>
<div class="projects-head">
  <div class="eyebrow" style="font-size:17px">פרויקטים</div>
  <div class="h2" style="color:#fff">הפרויקטים שלנו</div>
  <div class="rule"></div>
</div>

<div class="card-photo" style="left:712px;background:linear-gradient(180deg,#9fb4c9,#b7bfc7 40%,#8c9096 70%,#6d7174)" role="img" aria-label="מבנה תעשייה בפארק הטכנולוגי"></div>
<div class="card-photo" style="left:395px;background:linear-gradient(180deg,#d9b84a,#8fa4bd 35%,#6a7484 70%,#3e4a4f)" role="img" aria-label="חזית מרכז התחבורה"></div>
<div class="card-photo" style="left:80px;background:linear-gradient(180deg,#a9bfd4,#c7c3b2 30%,#6c8c5a 60%,#4f7a4a)" role="img" aria-label="צילום אווירי של פארק העיר והאגם"></div>

<div class="card-box" style="left:733px"><h3>מרכז העיר החדש</h3><p>פיתוח מרחב ציבורי חדש, נגיש ומזמין לכלל התושבים</p><span class="btn-green">קרא עוד</span></div>
<div class="card-box active" style="left:418px"><h3>מרכז העיר החדש</h3><p>פיתוח מרחב ציבורי חדש, נגיש ומזמין לכלל התושבים</p><span class="btn-green">קרא עוד</span></div>
<div class="card-box" style="left:99px"><h3>מרכז העיר החדש</h3><p>פיתוח מרחב ציבורי חדש, נגיש ומזמין לכלל התושבים</p><span class="btn-green">קרא עוד</span></div>

<div class="footer-bg"></div>
<section class="contact">
  <div class="eyebrow">צור קשר</div>
  <div class="h2">השאירו לנו הודעה</div>
  <div class="rule"></div>
  <p class="lead">מלאו את הפרטים ונציג מטעמנו יחזור אליכם בהקדם.</p>

  <div class="field" style="left:453px;top:157px;width:313px;height:48px"><svg viewBox="0 0 16 16"><circle cx="8" cy="5" r="3"/><path d="M2 15c0-4 12-4 12 0"/></svg>שם פרטי</div>
  <div class="field" style="left:129px;top:157px;width:313px;height:48px"><svg viewBox="0 0 16 16"><circle cx="8" cy="5" r="3"/><path d="M2 15c0-4 12-4 12 0"/></svg>שם משפחה</div>
  <div class="field" style="left:453px;top:215px;width:313px;height:48px"><svg viewBox="0 0 16 16"><path d="M3 2l3 1 1 3-2 1a8 8 0 0 0 4 4l1-2 3 1 1 3-2 1C7 14 2 9 2 4z"/></svg>טלפון</div>
  <div class="field" style="left:129px;top:215px;width:313px;height:48px"><svg viewBox="0 0 16 16"><rect x="2" y="4" width="12" height="9"/><path d="M2 4l6 5 6-5"/></svg>אימייל</div>
  <div class="field" style="left:129px;top:273px;width:637px;height:107px"><svg viewBox="0 0 16 16"><path d="M2 8c0-3 3-5 6-5s6 2 6 5-3 5-6 5l-4 2 1-3c-2-1-3-2-3-4z"/></svg>הודעה</div>
  <div class="send">שלח</div>
</section>

<div class="divider" style="left:132px"></div>
<div class="divider" style="left:442px"></div>
<div class="divider" style="left:730px"></div>

<div class="fcol" style="left:132px;width:266px">
  <h4>אודות</h4>
  <p>מנהלת תבור אחראית על ניהול פארק הטכנולוגיה (אלונים), מרכז בניין (הגפן), מרכז הבנייה, מרכז התחבורה, הכיכרות לכל אורכן ושלושת מרכזי הספורט והנופש.</p>
</div>
<div class="fcol" style="left:462px;width:268px">
  <h4>צור קשר</h4>
  <p><span class="ico-circle"><svg viewBox="0 0 16 16"><path d="M8 1a5 5 0 0 0-5 5c0 4 5 9 5 9s5-5 5-9a5 5 0 0 0-5-5zm0 7a2 2 0 1 1 0-4 2 2 0 0 1 0 4z"/></svg></span>שדרות הגפן 12, נווה תבור</p>
  <p style="margin-top:14px;display:flex;align-items:center"><span class="ico-circle"><svg viewBox="0 0 16 16"><path d="M3 1l3 1 1 3-2 1.5a8 8 0 0 0 4.5 4.5L11 9l3 1 1 3-2 2C7 15 1 9 1 3z"/></svg></span><span>טלפון 08-5550123<br>פקס 08-5550124</span></p>
</div>
<div class="fcol" style="left:760px;width:200px">
  <h4>קישורים</h4>
  <ul><li>לורם איפסום</li><li>DOLOR SIT AMET</li><li>CONSECTETUR ADIPISCING</li><li>ELIT ED DO EIUSMOD</li><li>תקנון האתר</li></ul>
</div>

<div class="to-top"><svg viewBox="0 0 32 32" width="32" height="32"><path d="M10 19l6-6 6 6" fill="none" stroke="#fff" stroke-width="2.5"/></svg></div>
<div class="copy">כל הזכויות שמורות ©www.tavor-city.co.il | גבעת הדר | נווה תבור - מנהלת תבור</div>

</body>
</html>
```